Simple, High-Class Web Design Wanted - Motivational Speakers Site

1. Full Brief/Request & Specs outlined on following video -
http://clipvane-recorder.com/watch/tbWrkLmQyP

2. Use colours, images as you feel suits objective (we are happy to pay up to US$30 for any good images but must have licence/permission).

3. Layout probably similar to existing site - www.podiumvoicehub.com.au / http://podiumvoicehub.com.au/contact.php

4. Must Be Able to Coded for MOBILE-FRIENDLINESS & WordPress friendly Ideal.

5. This is the first, small job of many we/graphic design jobs. If suits, winning designer may be offered all future work direct.

Thanks & look forward to your design. Glen.

Target Market(s)

corporates - high end

Number of Pages Required

2 page

Font styles to use
Sans Serif

Requirements
Must have
• Classy professional look
Nice to have
• all in Video in brief
Should not have
• too many images / new images I haven't approved

```html
<!DOCTYPE html>
<html lang="en">
<head>
<meta charset="utf-8">
<title>Speaker Suggestions / Speaker Help</title>
<link rel="stylesheet" href="https://fonts.googleapis.com/css2?family=Open+Sans:wght@400;600;800&family=Libre+Baskerville&display=swap">
<style>
  :root {
    --navy: #0e3d63;
    --green: #7cb530;
    --banner: #1b1b1b;
    --label: #444;
    --field-border: #cfcfcf;
    --note: #666;
    --page: #ffffff;
  }
  * { box-sizing: border-box; margin: 0; padding: 0; }
  html, body { width: 835px; height: 1200px; overflow: hidden; background: var(--page); }
  body { position: relative; font-family: "Open Sans", Arial, sans-serif; color: var(--label); }

  .headline { position: absolute; left: 70px; top: 26px; font-weight: 800; color: var(--navy); text-transform: uppercase; line-height: 1.05; font-size: 45px; letter-spacing: -0.3px; }
  .headline .dots { color: var(--green); }
  .headline .service { font-size: 20px; font-weight: 800; color: var(--navy); letter-spacing: 0; margin-left: 6px; }

  .banner { position: absolute; left: 70px; top: 175px; width: 695px; height: 42px; background: var(--banner); color: #fff; font-family: "Libre Baskerville", Georgia, serif; font-size: 22px; text-align: center; line-height: 42px; letter-spacing: 0.5px; }

  .intro { position: absolute; left: 120px; top: 228px; width: 600px; font-size: 9px; line-height: 1.5; color: var(--note); }
  .intro strong { color: var(--green); font-weight: 600; }
  .required { position: absolute; left: 120px; top: 272px; font-size: 10.5px; color: var(--green); font-weight: 600; }

  .row { position: absolute; left: 0; width: 835px; display: flex; align-items: center; }
  .row label { width: 305px; text-align: right; padding-right: 15px; font-size: 9.5px; color: var(--label); }
  .field { height: 22px; border: 1px solid var(--field-border); background: #fff; }
  .field.wide { width: 280px; }
  .field.textarea { height: 62px; width: 280px; }
  .field.textarea.short { height: 50px; }
  .field.small { width: 80px; }
  .field.half { width: 108px; }
  .select { position: relative; font-size: 8.5px; color: #999; padding-left: 6px; line-height: 20px; }
  .select svg { position: absolute; right: 6px; top: 8px; }
  .inline-label { font-size: 9.5px; margin: 0 6px 0 10px; }
  .gap { width: 8px; }

  .hint { position: absolute; left: 320px; font-size: 8.5px; color: var(--note); }
  .hint.green { color: var(--green); }

  .submit { position: absolute; left: 320px; top: 1066px; width: 72px; height: 24px; background: var(--green); color: #fff; font-size: 10px; font-weight: 600; text-align: center; line-height: 24px; }

  .footer-rule { position: absolute; left: 40px; top: 1148px; width: 755px; height: 1px; background: #e2e2e2; }
  .footer { position: absolute; left: 0; top: 1156px; width: 835px; text-align: center; font-size: 8.5px; color: var(--navy); }
  .page-no { position: absolute; right: 42px; top: 1156px; font-size: 8.5px; color: var(--navy); }
</style>
</head>
<body>
  <h1 class="headline">Find the speaker for your<br>Next event here <span class="dots">...</span><span class="service">Free industry service</span></h1>

  <div class="banner">SPEAKER SUGGESTIONS / SPEAKER HELP</div>

  <p class="intro"><strong>Note:</strong> Any information you provide on this form will only ever be used to reply to your enquiry. It will be treated only as an enquiry with no obligation and will never be used to send you unrelated mailings in the future.</p>
  <p class="required">* Required fields (just below the suggestions)</p>

  <div class="row" style="top:311px"><label>Subject *</label><div class="field wide select">Select subject<svg width="7" height="5" viewBox="0 0 7 5"><path d="M0 0h7L3.5 5z" fill="#999"/></svg></div></div>
  <div class="row" style="top:342px"><label>Company/Venue *</label><div class="field wide"></div></div>
  <div class="row" style="top:373px"><label>Expected date will be on *</label><div class="field wide"></div></div>
  <div class="row" style="top:406px"><label>State *</label><div class="field small select">State<svg width="7" height="5" viewBox="0 0 7 5"><path d="M0 0h7L3.5 5z" fill="#999"/></svg></div><span class="inline-label">Country *</span><div class="field small select">Country<svg width="7" height="5" viewBox="0 0 7 5"><path d="M0 0h7L3.5 5z" fill="#999"/></svg></div></div>
  <div class="row" style="top:460px"><label>The Specific Information<br>Type of Speaker We Would Like Is *</label><div class="field textarea"></div></div>
  <div class="row" style="top:545px"><label>First Name *</label><div class="field wide"></div></div>
  <div class="row" style="top:578px"><label>Last Name</label><div class="field wide"></div></div>
  <div class="row" style="top:611px"><label>Phone/Business</label><div class="field half"></div><div class="gap"></div><div class="field half"></div></div>
  <p class="hint green" style="top:640px">Note: can be useful if any problems with email</p>
  <div class="row" style="top:664px"><label>Phone/Mobile</label><div class="field wide"></div></div>
  <div class="row" style="top:701px"><label>Email *</label><div class="field wide"></div></div>
  <div class="row" style="top:740px"><label>Approximate Budget</label><div class="field wide select">Select approximate budget<svg width="7" height="5" viewBox="0 0 7 5"><path d="M0 0h7L3.5 5z" fill="#999"/></svg></div></div>
  <div class="row" style="top:779px"><label>Nature of Talk/Event Purpose</label><div class="field wide"></div></div>
  <div class="row" style="top:817px"><label>Type of Attendees</label><div class="field wide"></div></div>
  <p class="hint" style="top:846px">e.g. executives, staff, employees, mixed etc.</p>
  <div class="row" style="top:873px"><label>Expected Number</label><div class="field wide"></div></div>
  <div class="row" style="top:909px"><label>Duration of Talk</label><div class="field wide"></div></div>
  <div class="row" style="top:945px"><label>Talk Fees</label><div class="field wide"></div></div>
  <p class="hint" style="top:973px">Or 'Keen starting at'</p>
  <div class="row" style="top:993px"><label>Further Comments/Queries</label><div class="field textarea short"></div></div>

  <div class="submit">Submit</div>

  <div class="footer-rule"></div>
  <p class="footer">© 2015, Podium Voice Hub. All Rights Reserved</p>
  <span class="page-no">04</span>
</body>
</html>
```